Business Card Design for BrightlaneReach.com

--I need a business card design for my company BrightlaneReach.com

I have attached my logo...I want the brightlane reach logo on the front of the business card, and then I want The Brightlane Chief on the back of it with my information.

I would like to see a light colored background as well as a dark colored background

FRONT:
BRIGHTLANE REACH LOGO
247 E. Pelham Row
5th Floor
San Diego CA 92384
www.BrightlaneReach.com

Advanced Website & App Development
Websites, Apps, Online Voucher Systems

Leading Edge Marketing Services
SMS, VB, SMM, SEM,

BACK:
BRIGHTLANE CHIEF LOGO
Dorian Welker
The Brightlane Chief
Call Or Text: 555-204-3378
Dorian@BrightlaneChief.com
www.BrightlaneChief.com

Target Market(s)

small business owners

Industry/Entity Type

Business Consultant

Contact Information for Business Card

FRONT:
BRIGHTLANE REACH LOGO
247 E. Pelham Row
5th Floor
San Diego CA 92384
www.BrightlaneReach.com

SMS, VB, SMM, SEM,

BACK:
BRIGHTLANE CHIEF LOGO
Dorian Welker
The Brightlane Chief
Dorian@BrightlaneChief.com
www.BrightlaneChief.com

Requirements
Must have
• add this quote on it somewhere, anywhere,preferrably on back
• "The Fastest Way To Success Is To Take Action”
• — Dorian Welker, Brightlane Chief
Nice to have
• open
Should not have
• red

```html
<!DOCTYPE html>
<html lang="en">
<head>
<meta charset="utf-8">
<title>Brightlane Reach – Business Card</title>
<link rel="stylesheet" href="https://fonts.googleapis.com/css2?family=Oxanium:wght@400;500;600&display=swap">
<style>
  :root {
    --stage: #d9d9d9;
    --card-dark: #1f1e20;
    --card-light: #ffffff;
    --brand-blue: #1a6fae;
    --accent-blue: #2a86c8;
    --steel: #6f7276;
    --ink: #1c1c1c;
    --paper-text: #ffffff;
  }
  * { margin: 0; padding: 0; box-sizing: border-box; }
  html, body { width: 1200px; height: 900px; overflow: hidden; }
  body {
    background: var(--stage);
    font-family: "Oxanium", sans-serif;
    position: relative;
  }
  .card {
    position: absolute;
    left: 260px;
    width: 680px;
    height: 392px;
    overflow: hidden;
    box-shadow: 0 6px 18px rgba(0,0,0,.25);
  }

  /* ---------- Back (dark) ---------- */
  .card--back { top: 40px; background: var(--card-dark); }
  .back-logo {
    position: absolute; right: 70px; top: 26px; text-align: right;
  }
  .back-logo__name {
    font-size: 62px; font-weight: 500; color: var(--brand-blue);
    letter-spacing: 2px; line-height: 1;
  }
  .back-logo__sub {
    font-size: 26px; font-weight: 500; color: var(--steel);
    letter-spacing: 18px; margin-right: -18px; line-height: 1.2;
  }
  .quote-band {
    position: absolute; left: 0; right: 0; top: 128px; height: 56px;
    background: var(--brand-blue); color: var(--paper-text);
    display: flex; flex-direction: column; justify-content: center; align-items: center;
    font-style: italic; font-size: 15px; letter-spacing: 1px; line-height: 1.3;
  }
  .quote-band__author { padding-left: 40px; }
  .back-details {
    position: absolute; right: 46px; top: 202px; text-align: right;
  }
  .back-details__name {
    font-size: 36px; font-weight: 500; color: var(--accent-blue);
    letter-spacing: 2px; line-height: 1;
  }
  .back-details__title {
    font-size: 22px; color: var(--steel); letter-spacing: 2px; margin-bottom: 14px;
  }
  .contact-line {
    display: flex; justify-content: flex-end; align-items: center; gap: 10px;
    font-size: 18px; color: var(--steel); letter-spacing: 1px; line-height: 1.45;
  }
  .contact-line__highlight { color: var(--accent-blue); }
  .contact-icon { width: 18px; height: 18px; flex: none; }

  /* ---------- Front (light) ---------- */
  .card--front { top: 468px; background: var(--card-light); }
  .address-band {
    position: absolute; left: 0; right: 0; top: 18px; height: 78px;
    background: var(--brand-blue); color: var(--paper-text);
    display: flex; flex-direction: column; justify-content: center; align-items: center;
    font-size: 20px; letter-spacing: 1.5px; line-height: 1.3;
  }
  .front-url {
    position: absolute; left: 0; right: 0; top: 108px; text-align: center;
    font-size: 18px; color: var(--steel); letter-spacing: 1px;
  }
  .front-url__highlight { color: var(--brand-blue); }
  .front-logo {
    position: absolute; left: 0; right: 0; top: 134px; text-align: center;
  }
  .front-logo__name {
    font-size: 74px; font-weight: 500; color: var(--brand-blue);
    letter-spacing: 2px; line-height: 1;
  }
  .front-logo__sub {
    display: flex; align-items: center; justify-content: center; gap: 18px;
    font-size: 28px; font-weight: 500; color: var(--steel); letter-spacing: 8px;
    margin-top: 6px;
  }
  .front-logo__rule { width: 130px; height: 2px; background: var(--steel); }
  .services-band {
    position: absolute; left: 0; right: 0; top: 256px; height: 74px;
    background: var(--brand-blue); color: var(--paper-text);
    display: flex; flex-direction: column; justify-content: center; align-items: center;
    font-size: 21px; letter-spacing: 1px; line-height: 1.3;
  }
  .marketing-lines {
    position: absolute; left: 0; right: 0; top: 340px; text-align: center;
    font-size: 20px; color: var(--ink); letter-spacing: 1px; line-height: 1.2;
  }
</style>
</head>
<body>

<section class="card card--back" aria-label="Business card back">
  <div class="back-logo">
    <div class="back-logo__name">BRIGHTLANE</div>
    <div class="back-logo__sub">CHIEF</div>
  </div>

  <div class="quote-band">
    <p class="quote-band__text">“The Fastest Way To Success Is To Take Action”</p>
    <p class="quote-band__author">— Dorian Welker, Brightlane Chief</p>
  </div>

  <div class="back-details">
    <p class="back-details__name">DORIAN WELKER</p>
    <p class="back-details__title">The Brightlane Chief</p>
    <p class="contact-line">555-204-3378
      <svg class="contact-icon" viewBox="0 0 20 20" aria-hidden="true">
        <circle cx="10" cy="10" r="10" fill="var(--accent-blue)"/>
        <rect x="7" y="4.5" width="6" height="11" rx="1.2" fill="none" stroke="var(--card-dark)" stroke-width="1.4"/>
        <circle cx="10" cy="13.3" r=".8" fill="var(--card-dark)"/>
      </svg>
    </p>
    <p class="contact-line">Dorian@BrightlaneChief.com
      <svg class="contact-icon" viewBox="0 0 20 20" aria-hidden="true">
        <circle cx="10" cy="10" r="10" fill="var(--accent-blue)"/>
        <rect x="5" y="6.5" width="10" height="7" fill="none" stroke="var(--card-dark)" stroke-width="1.3"/>
        <polyline points="5,6.5 10,10.5 15,6.5" fill="none" stroke="var(--card-dark)" stroke-width="1.3"/>
      </svg>
    </p>
    <p class="contact-line">www.<span class="contact-line__highlight">BrightlaneChief</span>.com
      <svg class="contact-icon" viewBox="0 0 20 20" aria-hidden="true">
        <circle cx="10" cy="10" r="10" fill="var(--accent-blue)"/>
        <circle cx="10" cy="10" r="5.5" fill="none" stroke="var(--card-dark)" stroke-width="1.2"/>
        <ellipse cx="10" cy="10" rx="2.4" ry="5.5" fill="none" stroke="var(--card-dark)" stroke-width="1.2"/>
        <line x1="4.5" y1="10" x2="15.5" y2="10" stroke="var(--card-dark)" stroke-width="1.2"/>
      </svg>
    </p>
  </div>
</section>

<section class="card card--front" aria-label="Business card front">
  <div class="address-band">
    <p>247 E. Pelham Row, 5th Floor</p>
    <p>San Diego CA 92384</p>
  </div>

  <p class="front-url">www.<span class="front-url__highlight">BrightlaneReach</span>.com</p>

  <div class="front-logo">
    <div class="front-logo__name">BRIGHTLANE</div>
    <div class="front-logo__sub">
      <span class="front-logo__rule"></span>
      <span>REACH</span>
      <span class="front-logo__rule"></span>
    </div>
  </div>

  <div class="services-band">
    <p>Advanced Website &amp; App Development</p>
    <p>Websites, Apps, Online Voucher Systems</p>
  </div>

  <div class="marketing-lines">
    <p>Leading Edge Marketing Services</p>
    <p>SMS, VB, SMM, SEM,</p>
  </div>
</section>

</body>
</html>
```